Recruitment talent email to send employers

We are a recruitment company specialising in STEM talent. We're after an eye catching email design to send our clients (ie employers) information about our top cadidates.

Target Market(s)

Employers

Requirements
Must have
• Must be clean/fresh looking, professional and concise

```html
<!DOCTYPE html>
<html lang="en">
<head>
<meta charset="utf-8">
<title>Tessaline Talent – STEM Talent Email</title>
<link href="https://fonts.googleapis.com/css2?family=Jost:wght@300;400;500;600&display=swap" rel="stylesheet">
<style>
:root{
  --page:#edecec;
  --card:#ffffff;
  --orange:#e8552b;
  --orange-soft:#ee6a3f;
  --ink:#2d3640;
  --text:#5a5f66;
  --muted:#8c8c8c;
  --rule:#d6d6d6;
  --photo-hero-a:#3a3f44;
  --photo-hero-b:#6a6f73;
  --photo-side:#a3cbc9;
  --link:#c8102e;
}
*{box-sizing:border-box;margin:0;padding:0}
html,body{width:1200px;height:2442px;overflow:hidden}
body{background:var(--page);font-family:"Jost",sans-serif;color:var(--text);position:relative}
.abs{position:absolute}
.preheader{left:0;width:1200px;top:104px;text-align:center;font-family:Arial,Helvetica,sans-serif;font-size:20px;color:#444;line-height:26px}
.preheader a{color:var(--link);text-decoration:underline}
.card{left:231px;top:174px;width:741px;height:2097px;background:var(--card);border-radius:8px;box-shadow:0 10px 60px rgba(0,0,0,.08)}
.brand{display:flex;align-items:center;gap:14px;color:var(--ink);font-weight:600;white-space:nowrap}
.brand-mark{background:var(--orange);border-radius:4px}
.brand-header{left:0;width:741px;top:36px;justify-content:center;font-size:36px}
.brand-header .brand-mark{width:30px;height:30px}
.hero{left:28px;top:140px;width:680px;height:334px;overflow:hidden}
.hero-photo{left:0;top:0;width:680px;height:334px;background:linear-gradient(110deg,var(--photo-hero-a),var(--photo-hero-b) 60%,#b9b3aa)}
.hero-panel{left:0;top:0;width:300px;height:334px}
.hero-eyebrow{left:34px;top:126px;color:#fff;font-size:20px;font-weight:300}
.hero-title{left:32px;top:150px;color:#fff;font-size:37px;font-weight:500}
.hero-button{left:34px;top:215px;width:195px;height:57px;border:2px solid #fff;border-radius:29px;color:#fff;font-size:20px;font-weight:300;display:flex;align-items:center;justify-content:center}
.section-title{left:0;width:741px;text-align:center;font-size:29px;font-weight:500;color:var(--muted)}
.section-title .accent{color:var(--orange)}
.rule{left:29px;width:680px;height:1px;background:var(--rule)}
.block-heading{left:29px;width:405px;color:var(--ink);font-size:20px;font-weight:500;line-height:25px}
.bullets{left:29px;width:410px;list-style:none}
.bullets li{position:relative;padding-left:24px;font-size:18.5px;font-weight:300;line-height:28px;margin-bottom:11px}
.bullets li::before,.service-list li::before{content:"";position:absolute;left:2px;top:10px;width:7px;height:7px;border-right:1.5px solid var(--muted);border-top:1.5px solid var(--muted);transform:rotate(45deg)}
.side-photo{left:498px;top:596px;width:210px;height:386px;background:linear-gradient(180deg,var(--photo-side),#98c2c0)}
.more-button{left:54px;top:1003px;width:127px;height:46px;border:2px solid var(--orange);border-radius:24px;color:var(--orange);font-size:17px;font-weight:500;display:flex;align-items:center;justify-content:center}
.intro{left:29px;width:690px;top:1172px;font-size:21px;font-weight:300;line-height:30px}
.service-list{list-style:none;width:340px}
.service-list li{position:relative;padding-left:18px;font-size:18.5px;font-weight:500;color:var(--ink);line-height:24px;margin-bottom:13px}
.service-list li::before{border-color:var(--ink);border-width:2.5px;top:8px;left:0}
.step{width:200px;text-align:center;font-size:19px;font-weight:300}
.step-icon{display:block;margin:0 auto 16px}
.footer-brand{left:34px;top:1896px;font-size:24px;gap:10px}
.footer-brand .brand-mark{width:20px;height:20px}
.copyright{left:34px;top:1962px;font-size:19px;font-weight:300}
.social{left:30px;top:2000px;display:flex;gap:7px}
.contact{font-size:17.5px;font-weight:300;line-height:22px;color:var(--text)}
</style>
</head>
<body>
<p class="abs preheader">Is this email not displaying correctly?<br><a href="#">View it in your browser.</a></p>

<main class="abs card">
  <div class="abs brand brand-header"><span class="brand-mark" aria-hidden="true"></span>Tessaline Talent</div>

  <section class="abs hero">
    <div class="abs hero-photo" role="img" aria-label="Photo of a businessman presenting in a meeting room with sticky notes on a dark wall"></div>
    <svg class="abs hero-panel" width="300" height="334" viewBox="0 0 300 334" aria-hidden="true">
      <polygon points="0,0 220,0 294,167 220,334 0,334" fill="var(--orange-soft)"/>
    </svg>
    <p class="abs hero-eyebrow">Recruitment company</p>
    <h1 class="abs hero-title">STEM talent</h1>
    <a class="abs hero-button">Watch Our Site</a>
  </section>

  <h2 class="abs section-title" style="top:510px"><span class="accent">Working</span> Ways</h2>
  <div class="abs rule" style="top:567px"></div>

  <h3 class="abs block-heading" style="top:594px">ccusantium doloremque laudantium, totam rem aperiam, eaque ipsa</h3>
  <ul class="abs bullets" style="top:650px">
    <li>Lorem ipsum dolor sit amet, consectetur adipisicing elit, sed do eiusmod tempor</li>
    <li>voluptatem quia voluptas sit aspernatur aut odit aut fugit, sed quia consequuntur</li>
  </ul>
  <h3 class="abs block-heading" style="top:804px">qui dolorem ipsum quia dolor sit amet</h3>
  <ul class="abs bullets" style="top:846px">
    <li>Quasi architecto beatae</li>
    <li>oluptas sit aspernatur aut</li>
    <li>cillum dolore eu fugiat nulla pariatur.xcepteur sint occaecat cupidatat non proident</li>
  </ul>
  <div class="abs side-photo" role="img" aria-label="Photo of a smiling young woman pointing to the side against a teal wall"></div>
  <a class="abs more-button">More &gt;</a>

  <h2 class="abs section-title" style="top:1092px">Our <span class="accent">Services</span></h2>
  <div class="abs rule" style="top:1146px"></div>
  <p class="abs intro">We take the worry out of managing your back office with timely and reliable financial accounting services. We provide back office outsourcing services, monthly controllership functions and financial reporting services. Our services keep your back office functioning at its optimal level to minimize the worry of making uninformed business decisions.</p>
  <ul class="abs service-list" style="left:29px;top:1341px">
    <li>CFO Advisory Services</li>
    <li>Business Tax Compliance</li>
    <li>Non-Profit Compliance Oversight</li>
    <li>Accounting &amp; Bookkeeping</li>
    <li>Sales Tax Compliance</li>
  </ul>
  <ul class="abs service-list" style="left:396px;top:1341px">
    <li>Cross Border Managed Services</li>
    <li>Family Office Services</li>
    <li>Joint Defense Funds</li>
    <li>Individual Tax Compliance</li>
  </ul>

  <h2 class="abs section-title" style="top:1555px">Final <span class="accent">Work</span></h2>
  <div class="abs rule" style="top:1609px"></div>

  <div class="abs step" style="left:30px;top:1645px">
    <svg class="step-icon" width="86" height="86" viewBox="0 0 86 86" aria-hidden="true"><circle cx="43" cy="43" r="41" fill="none" stroke="var(--rule)" stroke-width="2"/><path d="M24 46 L62 24 L52 64 L42 50 Z M42 50 L62 24 M42 50 L40 62" fill="none" stroke="var(--muted)" stroke-width="2" stroke-linejoin="round"/></svg>
    Taken Document
  </div>
  <svg class="abs" style="left:196px;top:1658px" width="100" height="50" viewBox="0 0 100 50" aria-hidden="true"><path d="M4 44 Q40 0 92 18" fill="none" stroke="var(--orange)" stroke-width="2"/><path d="M82 10 L93 18 L82 24" fill="none" stroke="var(--orange)" stroke-width="2"/></svg>
  <div class="abs step" style="left:270px;top:1645px">
    <svg class="step-icon" width="86" height="86" viewBox="0 0 86 86" aria-hidden="true"><circle cx="43" cy="43" r="41" fill="none" stroke="var(--rule)" stroke-width="2"/><rect x="22" y="29" width="42" height="28" rx="4" fill="none" stroke="var(--muted)" stroke-width="2"/><rect x="28" y="34" width="30" height="18" fill="none" stroke="var(--muted)" stroke-width="1.5"/></svg>
    Analysis ourselves
  </div>
  <svg class="abs" style="left:440px;top:1658px" width="100" height="50" viewBox="0 0 100 50" aria-hidden="true"><path d="M4 34 Q50 54 92 10" fill="none" stroke="var(--orange)" stroke-width="2"/><path d="M80 10 L93 9 L92 22" fill="none" stroke="var(--orange)" stroke-width="2"/></svg>
  <div class="abs step" style="left:511px;top:1645px">
    <svg class="step-icon" width="86" height="86" viewBox="0 0 86 86" aria-hidden="true"><circle cx="43" cy="43" r="41" fill="none" stroke="var(--rule)" stroke-width="2"/><path d="M43 20 L62 27 V44 C62 56 52 63 43 67 C34 63 24 56 24 44 V27 Z" fill="none" stroke="var(--muted)" stroke-width="2"/><circle cx="43" cy="40" r="6" fill="none" stroke="var(--muted)" stroke-width="2"/><path d="M33 55 Q43 44 53 55" fill="none" stroke="var(--muted)" stroke-width="2"/></svg>
    Security
  </div>

  <div class="abs rule" style="top:1850px"></div>

  <div class="abs brand footer-brand"><span class="brand-mark" aria-hidden="true"></span>Tessaline Talent</div>
  <p class="abs copyright">© 2018 Coyright.</p>
  <div class="abs social" aria-label="Social links">
    <svg width="30" height="30" aria-hidden="true"><circle cx="15" cy="15" r="13.5" fill="none" stroke="var(--muted)" stroke-width="1.5"/></svg>
    <svg width="30" height="30" aria-hidden="true"><circle cx="15" cy="15" r="13.5" fill="none" stroke="var(--muted)" stroke-width="1.5"/></svg>
    <svg width="30" height="30" aria-hidden="true"><circle cx="15" cy="15" r="13.5" fill="none" stroke="var(--muted)" stroke-width="1.5"/></svg>
    <svg width="30" height="30" aria-hidden="true"><circle cx="15" cy="15" r="13.5" fill="none" stroke="var(--muted)" stroke-width="1.5"/></svg>
  </div>

  <svg class="abs" style="left:307px;top:1893px" width="40" height="40" viewBox="0 0 40 40" aria-hidden="true"><circle cx="20" cy="20" r="20" fill="var(--orange)"/><path d="M10 21 L20 12 L30 21 M14 18 V29 H26 V18" fill="none" stroke="#fff" stroke-width="2.5" stroke-linejoin="round"/><rect x="18" y="22" width="4" height="7" fill="#fff"/></svg>
  <p class="abs contact" style="left:308px;top:1944px">Westbrook Office<br>218 Harbor Lane<br>4th Floor<br>Westbrook, NY 10020</p>

  <svg class="abs" style="left:576px;top:1893px" width="40" height="40" viewBox="0 0 40 40" aria-hidden="true"><circle cx="20" cy="20" r="20" fill="var(--orange)"/><path d="M13 11 C11 13 11 17 14 22 C17 27 22 30 25 30 C27 30 29 28 29 27 L25 23 L22 25 C20 24 17 21 16 18 L18 15 Z" fill="#fff"/></svg>
  <p class="abs contact" style="left:575px;top:1948px">NY: 555.014.2270</p>
</main>
</body>
</html>
```